Website Design - Bright Harbor Vitality
Holistic Nutrition & Wellness Services
I want to thank everyone for their designs. You all do fabulous work and I look forward to perhaps running new contests in the future. I have made a decision for a design. Please know that there were several designs that I liked and considered.
Thanks again!!
Hello Designers,
Here is the sample data that can be added. It should be above the 4 services. (like the introduction to my site). The list of ailments can be within the same section or it can be a separate box/area on it's own.
Achieve your nutrition and wellness goals with the guidance and support of our Toronto Nutritionist. Whether your goal is to lose weight, reduce inflammation, lower cholesterol, minimize / eliminate diabetes, resolve digestive issues such as IBS, Acid Reflux and Constipation, or perhaps you simply wish to take preventive measures to ensure you remain healthy, a personalized nutritional consultation can help you restore balance to your body.
At Bright Harbor Vitality, we help guide you through the maze of information from books, magazines, supplements and diets on the market. Working one-on-one with our nutritionist, we help to identify and correct the nutritional causes of diseases. More…
Common Ailments that a Holistic Nutritionist can help with:
Acid Reflux
Allergies
Acne/Psoriasis/Eczema
Bloating / Gas
Brittle Hair & Nails
Constipation
Depression
Eczema/Acne/Psoriasis
Fatigue
Heart Burn
Hormonal Imbalances
Hot Flashes
High Blood Pressure
High Cholesterol
Insomnia
PMS
Stress/Anxiety
Here is sample data/information that can go in the 4 sections you will create to show our Key Services:
Nutritional Consulting Services
Resolve the underlying causes of your typical health ailments such as acid reflux, gas & bloating; improve your health and make better food choices with the guidance of our Toronto Nutritionist. More….
Weight Loss Services
Transform your body one bite at a time. Lose weight and keep it off. With the guidance and support of our Toronto Nutritionist, our weight loss transformation program is personalized to fit your needs and current health situation. More….
Nutritional Supplementation
Learn the smart and safe way to take dietary supplements and vitamins. Our Toronto Nutritionist will review your current supplementation program and make recommendations based upon your current health and supplementation needs. More….
Wellness Lectures/Seminars
We believe that wellness, inside and out is best achieved through life long education. Our wellness lectures & seminars provide you with valuable information on building healthy lifestyle practices as well as giving you the practical tools to take result oriented action. More…
I appreciate the designs submitted thus far, but they are not quite what I am looking for yet. I have browsed some of the other pixelcrowd projects online to see if there are some layouts that I like. Please take a look at the following designs which might help give you a better idea:
Draft #50 for Amber Ridge Finance Project - I like the individual boxes used to display the information. I would like my key services displayed in such a manner. Each box will have a bit of information displayed along with a photo and then a link to the detailed information.
Draft #12 & Draft #52 for Vigor Bargains Project
The following info summarizes the brief requirements (this summary includes some updates not previously indicated in earlier comments):
• In the area where my logo is, please include Nutrition & Wellness Services with the tag line “Achieving wellness, one bite at a time”
• The main body of the page should clearly convey the key services we provide with links to subsequent detailed pages. These are not just captions with links, but will have a bit of information included, perhaps with a suitable image:
o Nutritional Consulting
o Weight Loss
o Nutritional Supplementation
o Wellness Lectures/Seminars
• Main Navigation bar should have:
o Home
o Services
o About
o Tools
o Contact
I would like a section/box where I will insert a Featured Seminar/Lecture Video. There should be a link where the client can Register for an upcoming Seminar/Lecture. There should be a link on the page where clients can Sign Up to receive Updates on Upcoming Seminars/Lectures
Phone number; email address; and a link to BOOK YOUR APPOINTMENT should be clearly visible on main page and every subsequent page.
Main Page should include a BUY TAB/LINK for clients to purchase GIFT CERTIFICATES "Give the gift of Health"
Repeat navigation in the footer; footer should also have sitemap; Terms of Service;
Thanks for your patience. This is my first time submitting a brief.
Designers,
Update to brief:
Please include a section that enables clients to buy GIFT CERTIFICATES.
For example:
Give the gift of Health
GIFT CERTIFICATES
There should also be a link or an area where clients may enter their email address in order to be added to our distribution list advising them of upcoming seminars/workshops
SIGN UP TO RECEIVE UPDATES TO UPCOMING SEMINARS/WORKSHOPS
Thank you for your submissions thus far. Dolvetik: I like the black background with my logo and the partial silouette of my logo. I also like the picture you used. Can you adjust the navigation bar to reflect my notes in my comments applied at 9:07 am Nov 24th. Also would like to see the four services as separate boxes within the body of the page so that users can easily see these 'KEY' services that we offer.
Thanks kindly.
Main services that will be offered are:
Nutritional Consulting
Weight Loss
Wellness Seminars/Workshops
These should be prominently displayed so that people do not need to read a lot of information or click many tabs to KNOW that these are the MAIN services offered. Detailed information for each service would be under the SERVICES navigation tab. I would like potential clients to be able to click from the main page to access these services.
The main page should have a BOOK YOUR APPOINTMENT (which will link to a form) and our phone number prominently displayed.
The main navigation bar should have:
Home
Services
About
Tools
Contact
The following two websites are examples of my competitors. Naturally, I would want my website to be far superior to theirs:
ninacrossfoods.example
www.leahvinter.example
I like the look and feel of this website but not the colors:
www.glowmerabeauty.example
I would like to see some designs with my logo in the black background. I think the blues and greens really pop with the black background. My business card will also be printed using the black background.
Thanks very much for your submissions are hard work.
Attention Designers !
You are required to design the main page template only. Final art work will be required in PSD format.

```html
<!DOCTYPE html>
<html lang="en">
<head>
<meta charset="utf-8">
<title>Bright Harbor Vitality – Home</title>
<link href="https://fonts.googleapis.com/css2?family=Arimo:wght@400;700&display=swap" rel="stylesheet">
<style>
  :root {
    --green: #4f9a1c;
    --green-dark: #3a7d10;
    --green-light: #8cc63f;
    --blue: #1c5fb8;
    --text: #555555;
    --nav-bg: #f1f1f1;
    --nav-line: #d6d6d6;
    --border: #cfcfcf;
    --white: #ffffff;
  }
  * { margin: 0; padding: 0; box-sizing: border-box; }
  html, body { width: 1200px; height: 871px; overflow: hidden; background: var(--white); }
  body { font-family: 'Arimo', Arial, sans-serif; color: var(--text); position: relative; }

  .brand { position: absolute; left: 112px; top: 30px; display: flex; align-items: center; gap: 16px; }
  .brand-dot { width: 56px; height: 56px; border-radius: 50%; background: var(--green-light); }
  .brand-name { font-size: 34px; font-weight: 700; color: var(--blue); }

  .main-nav { position: absolute; left: 112px; top: 142px; width: 988px; height: 58px;
    background: linear-gradient(#fafafa, var(--nav-bg)); border-top: 1px solid var(--nav-line);
    display: flex; align-items: center; font-size: 16px; text-transform: uppercase; color: #333; }
  .main-nav a { color: inherit; text-decoration: none; padding: 0 14px; }
  .main-nav .sep { color: #777; }
  .main-nav .active { background: var(--green); color: var(--white); height: 100%;
    width: 108px; display: flex; align-items: center; justify-content: center; padding: 0; margin-right: 24px; }

  .hero { position: absolute; left: 112px; top: 200px; width: 988px; height: 332px; display: flex; }
  .hero-image { width: 563px; height: 100%;
    background: radial-gradient(circle at 60% 45%, #e8f2d6 0%, #a7cf6a 35%, #5f9a24 75%, #3f7a14 100%); position: relative; }
  .hero-button { position: absolute; left: 88px; top: 298px; width: 72px; height: 26px; border-radius: 4px;
    background: var(--green-light); border: 1px solid #6aa52a; color: var(--white); font-size: 12px;
    display: flex; align-items: center; justify-content: center; text-decoration: none; }
  .hero-about { flex: 1; background: linear-gradient(#5fa91f, #3f8c12); color: var(--white); padding: 14px 18px 0 22px; }
  .hero-about h1 { font-size: 40px; font-weight: 400; margin-bottom: 14px; }
  .hero-about p { font-size: 14px; line-height: 17px; margin-bottom: 17px; }

  .divider { position: absolute; left: 112px; top: 532px; width: 988px; height: 12px; background: #eeeeee; }

  .panel { position: absolute; top: 546px; height: 280px; border: 1px solid var(--border); }
  .panel h2 { font-size: 30px; font-weight: 400; color: var(--green-dark); padding: 4px 6px; border-bottom: 1px solid var(--border); }
  .panel-life { left: 112px; width: 550px; }
  .panel-news { left: 672px; width: 428px; }
  .life-body { padding: 6px 4px; font-size: 14px; line-height: 16px; }
  .life-image { float: left; width: 186px; height: 124px; margin: 2px 8px 2px 0;
    background: linear-gradient(135deg, #c9a23a, #7a9a3a 50%, #b8482a); }
  .news-list { list-style: none; padding: 6px 6px; font-size: 14px; line-height: 17px; }

  .footer-bar { position: absolute; left: 112px; top: 838px; width: 988px; height: 12px; background: var(--green); }
  .copyright { position: absolute; left: 0; top: 856px; width: 1200px; text-align: center; font-size: 12px; color: #888; }
</style>
</head>
<body>
  <header class="brand">
    <span class="brand-dot"></span>
    <span class="brand-name">Bright Harbor Vitality</span>
  </header>

  <nav class="main-nav">
    <a class="active" href="#">Home</a>
    <a href="#">Nutritional Consulting</a><span class="sep">|</span>
    <a href="#">Weightloss Services</a><span class="sep">|</span>
    <a href="#">Workshops/Seminars</a><span class="sep">|</span>
    <a href="#">About Us</a><span class="sep">|</span>
    <a href="#">Contact Us</a>
  </nav>

  <section class="hero">
    <div class="hero-image" role="img" aria-label="Mortar and pestle with fresh green herbs and a natural product badge">
      <a class="hero-button" href="#">Click here</a>
    </div>
    <div class="hero-about">
      <h1>About Company</h1>
      <p>Mainstream medicine does not emphasize the significance of poor nutrition as a major cause of a wide range of health disorders. Although most people are aware of the benefits of sound nutrition, the range of conflicting information available to the consumer is often confusing.</p>
      <p>At Bright Harbor Vitality, we help guide our clients through the maze of information from books, magazines, supplements and diet and lifestyle programs.</p>
      <p>We work one-on-one with our clients to identify and help correct the nutritional causes of diseases. Through personalized diet and lifestyle programs, we help our clients optimize health and achieve balance.</p>
    </div>
  </section>

  <div class="divider"></div>

  <section class="panel panel-life">
    <h2>Change our life with us</h2>
    <div class="life-body">
      <div class="life-image" role="img" aria-label="Fresh fruit and vegetables at a market stall"></div>
      Mainstream medicine does not emphasize the significance of poor nutrition as a major cause of a wide range of health disorders. Although most people are aware of the benefits of sound nutrition, the range of conflicting information available to the consumer is often confusing.
      At Bright Harbor Vitality, we help guide our clients through the maze of information from books, magazines, supplements and diets on the market.
      We work one-on-one with our clients to identify and help correct the nutritional causes of diseases. Through personalized diet and lifestyle programs, we help our clients optimize health and achieve balance.
    </div>
  </section>

  <section class="panel panel-news">
    <h2>NEWS AND Featured</h2>
    <ul class="news-list">
      <li>Weight Loss Diet</li>
      <li>Molestie lacus. Aenean nonummy hendrerit mauris pellus.</li>
      <li>Help Me Lose Weight Fast</li>
      <li>Aenean nonummy hendrerit mauris. Phasellus porta. Fusce suscipit.</li>
      <li>Losing Weight Fast</li>
      <li>Aenean auctor wisi et urna aliquam.</li>
      <li>Lose Weight in a Month</li>
      <li>Aenean nonummy hendrerit mauris. Phasellus porta. Fusce suscipit.</li>
    </ul>
  </section>

  <div class="footer-bar"></div>
  <footer class="copyright">© 2011 BHV . All Rights Reserved.</footer>
</body>
</html>
```